Business Postcard to attract business listings on directory

We need a postcard that professionally and excitedly highlights the benefits of getting listed on our local business directory.

Our local business directory combines a Quarterly direct mail piece a LOCAL discount card, which means no coupons for people to remember to use, and the power of an online directory and the benefits of local SEO.

Colorful, Vector/Images and Bold text a must

Target Market(s)

Local business, all industrys that service the public, retail,food, construction,plumbing etc.

Industry/Entity Type

Business Directory

Font styles to use
Other font styles liked:
• Calibri,Verdana

Requirements
Must have
• High Quality Graphics
• Vector Icons
• Vibrant Professional Colors
• Place for my contact details
Nice to have
• Some kind of business guy, Cartoonish maybe flying or "exploding" with new business sales
Should not have
• Excessive Blank Space

```html
<!DOCTYPE html>
<html lang="en">
<head>
<meta charset="utf-8">
<title>Benefits of Listing – Postcard</title>
<link rel="stylesheet" href="https://fonts.googleapis.com/css2?family=Montserrat:wght@400;500;700;800&family=Arvo:wght@700&family=Lobster+Two:ital,wght@1,700&display=swap">
<style>
  :root{
    --backdrop:#353535;
    --blue:#1b5db3;
    --blue-deep:#16468f;
    --orange:#f5a11e;
    --orange-deep:#ef7a22;
    --navy:#1c3a8a;
    --white:#ffffff;
  }
  *{margin:0;padding:0;box-sizing:border-box}
  html,body{width:1200px;height:996px;overflow:hidden}
  body{background:var(--backdrop);position:relative;font-family:"Montserrat",Verdana,sans-serif}
  .postcard{position:absolute;left:61px;top:84px;width:1079px;height:829px;background:var(--white);overflow:hidden;box-shadow:0 10px 30px rgba(0,0,0,.55)}
  .postcard__shapes{position:absolute;inset:0}
  .heading-kicker{position:absolute;left:38px;top:24px;width:367px;display:flex;align-items:center;gap:12px;color:var(--orange);font-weight:500;font-size:32px;letter-spacing:1px;line-height:1}
  .heading-kicker::before,.heading-kicker::after{content:"";flex:1;height:5px;background:var(--orange)}
  .heading-banner{position:absolute;left:38px;top:56px;width:450px;height:63px}
  .heading-title{position:absolute;left:98px;top:66px;font-family:"Arvo",Georgia,serif;font-weight:700;font-size:40px;color:var(--white);letter-spacing:1px;line-height:1}
  .benefit{position:absolute;left:82px;color:var(--white);font-size:28px;line-height:35px;white-space:nowrap}
  .benefit b{font-weight:800}
  .benefit__tick{position:absolute;left:-43px;top:3px;width:29px;height:29px}
  .call-bar{position:absolute;left:63px;top:650px;width:432px;height:60px;border-radius:30px;background:linear-gradient(90deg,var(--orange),var(--orange-deep));box-shadow:0 6px 10px rgba(0,0,0,.35)}
  .call-bar__icon{position:absolute;left:4px;top:3px;width:54px;height:54px;border-radius:50%;background:var(--white);display:flex;align-items:center;justify-content:center}
  .call-bar__text{position:absolute;left:68px;top:8px;font-family:"Lobster Two",cursive;font-style:italic;font-weight:700;font-size:35px;color:var(--navy);line-height:44px;white-space:nowrap}
  .map-art{position:absolute;left:86px;top:722px;width:101px;height:54px;background:linear-gradient(135deg,#e8efe6,#b9cfb5);transform:skewY(-6deg)}
  .company-name{position:absolute;left:191px;top:746px;font-weight:800;font-size:24px;color:var(--white);line-height:30px;white-space:nowrap}
  .company-address{position:absolute;left:78px;top:779px;font-size:24px;color:var(--white);line-height:30px;white-space:nowrap}
  .company-address b{font-weight:800}
</style>
</head>
<body>
<main class="postcard">
  <svg class="postcard__shapes" viewBox="0 0 1079 829" width="1079" height="829" aria-hidden="true">
    <defs>
      <linearGradient id="panelBlue" x1="0" y1="0" x2="1" y2="0">
        <stop offset="0" stop-color="#1c5fb6"/>
        <stop offset=".75" stop-color="#1a57aa"/>
        <stop offset="1" stop-color="#163f85"/>
      </linearGradient>
    </defs>
    <path d="M0 0H502C540 200 630 420 640 650C644 740 612 800 579 829H0Z" fill="url(#panelBlue)"/>
    <path d="M526 0H541C602 250 700 500 685 700C680 770 670 800 663 829H603C632 780 648 720 648 650C643 420 562 200 526 0Z" fill="var(--orange)"/>
  </svg>

  <div class="heading-kicker">BENEFITS</div>
  <svg class="heading-banner" viewBox="0 0 450 63" aria-hidden="true">
    <defs>
      <linearGradient id="bannerGrad" x1="0" y1="0" x2="1" y2="0">
        <stop offset="0" stop-color="var(--orange-deep)"/>
        <stop offset="1" stop-color="var(--orange)"/>
      </linearGradient>
    </defs>
    <path d="M0 0H367L420 63H0Z" fill="url(#bannerGrad)"/>
    <path d="M390 31H445L420 63Z" fill="var(--orange-deep)"/>
  </svg>
  <div class="heading-title">OF LISTING</div>

  <div class="benefit" style="top:145px"><svg class="benefit__tick" viewBox="0 0 30 30"><circle cx="15" cy="15" r="15" fill="var(--orange)"/><path d="M8 15l5 5 9-10" fill="none" stroke="var(--blue)" stroke-width="3.2" stroke-linecap="round" stroke-linejoin="round"/></svg><b>MORE</b> FOOT TRAFFIC</div>
  <div class="benefit" style="top:186px"><svg class="benefit__tick" viewBox="0 0 30 30"><circle cx="15" cy="15" r="15" fill="var(--orange)"/><path d="M8 15l5 5 9-10" fill="none" stroke="var(--blue)" stroke-width="3.2" stroke-linecap="round" stroke-linejoin="round"/></svg>Quarterly Mailing<br>To <b>10,000 local shoppers</b></div>
  <div class="benefit" style="top:260px"><svg class="benefit__tick" viewBox="0 0 30 30"><circle cx="15" cy="15" r="15" fill="var(--orange)"/><path d="M8 15l5 5 9-10" fill="none" stroke="var(--blue)" stroke-width="3.2" stroke-linecap="round" stroke-linejoin="round"/></svg>Desktop &amp; Mobile<br><b>optimized online listing</b></div>
  <div class="benefit" style="top:335px"><svg class="benefit__tick" viewBox="0 0 30 30"><circle cx="15" cy="15" r="15" fill="var(--orange)"/><path d="M8 15l5 5 9-10" fill="none" stroke="var(--blue)" stroke-width="3.2" stroke-linecap="round" stroke-linejoin="round"/></svg><b>Show up</b><br>in Search Engine Results</div>
  <div class="benefit" style="top:411px"><svg class="benefit__tick" viewBox="0 0 30 30"><circle cx="15" cy="15" r="15" fill="var(--orange)"/><path d="M8 15l5 5 9-10" fill="none" stroke="var(--blue)" stroke-width="3.2" stroke-linecap="round" stroke-linejoin="round"/></svg><b>List Active</b> Coupons &amp; Deals</div>
  <div class="benefit" style="top:452px"><svg class="benefit__tick" viewBox="0 0 30 30"><circle cx="15" cy="15" r="15" fill="var(--orange)"/><path d="M8 15l5 5 9-10" fill="none" stroke="var(--blue)" stroke-width="3.2" stroke-linecap="round" stroke-linejoin="round"/></svg><b>Connect Direct</b> With Shoppers</div>
  <div class="benefit" style="top:492px"><svg class="benefit__tick" viewBox="0 0 30 30"><circle cx="15" cy="15" r="15" fill="var(--orange)"/><path d="M8 15l5 5 9-10" fill="none" stroke="var(--blue)" stroke-width="3.2" stroke-linecap="round" stroke-linejoin="round"/></svg><b>Support Local Shoppers</b><br>with the <b>LOCAL</b> Discount Card</div>
  <div class="benefit" style="top:567px"><svg class="benefit__tick" viewBox="0 0 30 30"><circle cx="15" cy="15" r="15" fill="var(--orange)"/><path d="M8 15l5 5 9-10" fill="none" stroke="var(--blue)" stroke-width="3.2" stroke-linecap="round" stroke-linejoin="round"/></svg>Dedicated Account Manager<br>Handles <b>everything</b> for you</div>

  <div class="call-bar">
    <div class="call-bar__icon">
      <svg width="34" height="34" viewBox="0 0 34 34" aria-hidden="true">
        <path d="M4 12c0-5 6-8 13-8s13 3 13 8v3h-7v-3c-2-1-4-1.5-6-1.5S13 11 11 12v3H4Z" fill="var(--blue)"/>
        <path d="M8 17h18l3 12H5Z" fill="var(--blue)"/>
        <circle cx="17" cy="23" r="3.5" fill="var(--white)"/>
      </svg>
    </div>
    <div class="call-bar__text">Call Us: 1 555 014 2290</div>
  </div>

  <div class="map-art" role="img" aria-label="Folded street map with a location pin"></div>
  <div class="company-name">Harbor Post Partners</div>
  <div class="company-address">P.O Box <b>418</b>, Millbrook, CT <b>06099</b></div>
</main>
</body>
</html>
```